Need a professional card design. Tallowmere building company specialise in residential and commercial builds. New homes, additions & renovations.
Wanting a card with creativity and professionalism.
Want card that utilises logo.

Back and front.

I have just created a logo, and want to use it on the business card.
Attached a copy of the logo.
Attached is also a current business card which I wish to redesign

please utilise both sides

Residential

• Reg# 58306

```html
<!DOCTYPE html>
<html lang="en">
<head>
<meta charset="utf-8">
<title>Tallowmere Building Company – Business Cards</title>
<link href="https://fonts.googleapis.com/css2?family=EB+Garamond:wght@400;500&display=swap" rel="stylesheet">
<style>
  :root {
    --backdrop: #e9e6e1;
    --card: #ffffff;
    --ink: #1c1a18;
    --accent: #efa73a;
    --rule: #cfcac3;
  }
  * { box-sizing: border-box; margin: 0; padding: 0; }
  html, body {
    width: 1200px; height: 675px; overflow: hidden;
    background: var(--backdrop);
    font-family: "EB Garamond", Georgia, serif;
    color: var(--ink);
  }
  .sheet {
    width: 1200px; height: 675px;
    display: flex; align-items: center; justify-content: center; gap: 40px;
  }
  .card {
    position: relative;
    width: 540px; height: 300px;
    background: var(--card);
    box-shadow: 0 4px 14px rgba(0,0,0,.15);
    overflow: hidden;
  }
  .stripes { position: absolute; left: 0; right: 0; bottom: 0; }
  .stripes .dark { height: 8px; background: var(--ink); }
  .stripes .gap { height: 5px; background: var(--card); }
  .stripes .band { height: 26px; background: var(--accent); }

  .wordmark { display: flex; align-items: center; gap: 10px; }
  .wordmark .mark { width: 14px; height: 14px; border-radius: 50%; background: var(--accent); flex: none; }
  .wordmark .name {
    font-size: 30px; font-weight: 500; line-height: 1.05; color: var(--ink);
    letter-spacing: .5px;
  }
  .reg { font-size: 13px; letter-spacing: .3px; }

  /* front */
  .front .wordmark { position: absolute; left: 0; right: 0; top: 74px; justify-content: center; }
  .front .name { text-align: center; }
  .front .reg { position: absolute; left: 0; right: 0; top: 160px; text-align: center; }
  .front .tagline {
    position: absolute; left: 18px; bottom: 54px;
    font-size: 16.5px;
  }

  /* back */
  .back .wordmark { position: absolute; left: 26px; top: 98px; width: 240px; }
  .back .name { font-size: 27px; }
  .back .divider { position: absolute; left: 272px; top: 36px; height: 194px; border-left: 1px solid var(--rule); }
  .back .reg { position: absolute; left: 86px; top: 226px; }
  .back .person { position: absolute; right: 48px; top: 46px; text-align: right; }
  .back .person .full-name { font-size: 18px; color: var(--accent); letter-spacing: .5px; text-transform: uppercase; }
  .back .person .role { font-size: 12.5px; letter-spacing: .4px; }
  .back .contact {
    position: absolute; right: 48px; top: 140px; text-align: right;
    font-size: 12.5px; line-height: 1.35; list-style: none;
  }
</style>
</head>
<body>
<main class="sheet">
  <section class="card front" aria-label="Card front">
    <div class="wordmark">
      <span class="mark"></span>
      <span class="name">Tallowmere<br>building company</span>
    </div>
    <p class="reg">REG.No 58306</p>
    <p class="tagline">New homes - addition &amp; renovations domestic &amp; commercial builders</p>
    <div class="stripes"><div class="dark"></div><div class="gap"></div><div class="band"></div></div>
  </section>

  <section class="card back" aria-label="Card back">
    <div class="wordmark">
      <span class="mark"></span>
      <span class="name">Tallowmere<br>building company</span>
    </div>
    <span class="divider"></span>
    <p class="reg">REG.No 58306</p>
    <div class="person">
      <p class="full-name">Mara Ellison</p>
      <p class="role">DIRECTOR</p>
    </div>
    <ul class="contact">
      <li>42 Harwick Lane</li>
      <li>Elmsford WA, 6031</li>
      <li>TELL: 08 9412 3586</li>
      <li>FAX: 08 9412 3586</li>
      <li>CELL: 0422 618 904</li>
      <li>tallowmerebuilding@mailbox.com</li>
    </ul>
    <div class="stripes"><div class="dark"></div><div class="gap"></div><div class="band"></div></div>
  </section>
</main>
</body>
</html>
```